Need a new letterhead

Need a new fresh exciting letterhead. Remove the footer...info is outdated.

Target Market(s)

B2B

Industry/Entity Type

Electrical Power

Colors

Designer to choose colors to be used in the design.

Requirements
Must have
• Red and Blue Brindlecroft Arcwell Logo
Nice to have
• Lighting the way to sustainability in footer...reorganize the words?

```html
<!DOCTYPE html>
<html lang="en">
<head>
<meta charset="utf-8">
<title>Brindlecroft Arcwell Letterhead</title>
<link rel="stylesheet" href="https://fonts.googleapis.com/css2?family=Open+Sans:wght@400;800&display=swap">
<style>
  :root {
    --backdrop: #e9e6e2;
    --paper: #ffffff;
    --brand-red: #ed1c24;
    --brand-blue: #283a8e;
    --ink: #3a3a3a;
    --icon: #5a6796;
    --badge-line: #8a8a8a;
    --badge-sun: #f5c400;
  }
  * { box-sizing: border-box; margin: 0; padding: 0; }
  html, body {
    width: 1200px; height: 1085px; overflow: hidden;
    background: var(--backdrop);
    font-family: "Open Sans", sans-serif;
  }
  .letterhead {
    position: absolute; left: 240px; top: 30px;
    width: 721px; height: 1025px;
    background: var(--paper);
    box-shadow: 0 4px 18px rgba(0,0,0,.18);
  }
  .brand-name {
    position: absolute; left: 50px; top: 48px;
    color: var(--brand-red);
    font-weight: 800; font-size: 30px; line-height: 34px;
    letter-spacing: .5px;
  }
  .footer-band { position: absolute; left: 0; top: 922px; width: 721px; height: 103px; }
  .contact-list { position: absolute; left: 50px; top: 936px; list-style: none; }
  .contact-item {
    display: flex; align-items: center; gap: 7px;
    height: 21px; font-size: 13px; color: var(--ink);
  }
  .contact-item svg { width: 13px; height: 13px; flex: none; }
  .postal-address {
    position: absolute; left: 326px; top: 942px;
    font-size: 13px; line-height: 19px; color: var(--ink); font-style: normal;
  }
  .tagline-badge {
    position: absolute; left: 534px; top: 940px;
    width: 136px; height: 56px;
    border: 1px solid var(--badge-line);
  }
  .tagline-badge .badge-dot {
    position: absolute; right: 10px; top: 12px;
    width: 30px; height: 30px; border-radius: 50%;
    background: var(--badge-sun);
  }
</style>
</head>
<body>
  <main class="letterhead">
    <header class="brand-name">Brindlecroft<br>Arcwell</header>

    <svg class="footer-band" viewBox="0 0 721 103" aria-hidden="true">
      <polygon fill="var(--brand-red)" points="0,0 18,19 18,83 325,83 325,103 0,103"/>
      <polygon fill="var(--brand-blue)" points="721,0 703,19 703,83 325,83 325,103 721,103"/>
    </svg>

    <ul class="contact-list">
      <li class="contact-item">
        <svg viewBox="0 0 16 16" fill="none" stroke="var(--icon)" stroke-width="1.2"><path d="M4 1.5l2.5 3-1.5 1.8c.8 1.8 2.2 3.2 4 4l1.8-1.5 3 2.5-1.5 2.2C7 13.5 2.5 9 1.8 3z"/></svg>
        <span>555-014-2290</span>
      </li>
      <li class="contact-item">
        <svg viewBox="0 0 16 16" fill="none" stroke="var(--icon)" stroke-width="1.2"><rect x="4" y="1.5" width="8" height="4"/><rect x="1.5" y="5.5" width="13" height="6"/><rect x="4" y="9" width="8" height="5.5"/></svg>
        <span>555-014-2291</span>
      </li>
      <li class="contact-item">
        <svg viewBox="0 0 16 16" fill="none" stroke="var(--icon)" stroke-width="1.2"><circle cx="8" cy="8" r="6.5"/><ellipse cx="8" cy="8" rx="3" ry="6.5"/><path d="M1.5 8h13M2.5 4.8h11M2.5 11.2h11"/></svg>
        <span>www.BrindlecroftArcwell.com</span>
      </li>
    </ul>

    <address class="postal-address">417 Halvern<br>Avenue Dunmore Falls,<br>Ohio 43990</address>

    <div class="tagline-badge" role="img" aria-label="Sustainability badge">
      <span class="badge-dot"></span>
    </div>
  </main>
</body>
</html>
```